Flat bootstrap design for existing site

I'm looking for a modern flat design based around an existing logo. This has to be a custom design (no external templates), and implemented into a bootstrap framework.

The logo is attached as 2 versions - choose whichever you want, that flows better with whatever design you choose.

Added screenshots of the existing site (currently using the default bootstrap layouts). Please make your designs around those pages in the screenshots (i.e. the homepage only has the postal code input and the header). The active page has 3 screenshots, because I wanted to illustrate the other states that would be visible (in the table rows).

This is a moving/junk removal website, just for some context.

Here's some example websites (flat designs) that I like, just to give you an idea of what I'm after.

https://www.plivoterra.com/
https://damsoqua.com/
https://trevalin.com/
https://morkadelphi.com/en/

Coding

Coded - Design and coding required

Number of Pages Required

5+ page

Colors

Designer to choose colors to be used in the design.

Requirements
Must have
• It must be a modern/simple flat design, that is built around the existing logo (attached).
• It has to be implemented using bootstrap.

```html
<!DOCTYPE html>
<html lang="en">
<head>
<meta charset="utf-8">
<title>Haulvo – Book Junk Removal</title>
<link href="https://fonts.googleapis.com/css2?family=Roboto:wght@400;500;700&display=swap" rel="stylesheet">
<style>
  :root {
    --brand-blue: #4bc9f4;
    --brand-blue-dark: #3fb8e2;
    --page-bg: #f7f7f7;
    --panel-bg: #ffffff;
    --panel-border: #dcdcdc;
    --heading-grey: #555555;
    --input-border: #d4d4d4;
    --placeholder-grey: #777777;
    --footer-bg: #5a5a5a;
    --white: #ffffff;
  }
  * { box-sizing: border-box; margin: 0; padding: 0; }
  html, body { width: 1200px; height: 557px; overflow: hidden; }
  body {
    font-family: "Roboto", Arial, sans-serif;
    background: var(--page-bg);
    position: relative;
  }
  .site-header {
    position: absolute; left: 0; top: 0;
    width: 1200px; height: 88px;
    background: var(--brand-blue);
  }
  .brand {
    position: absolute; left: 86px; top: 24px;
    color: var(--white);
    font-weight: 700; font-size: 36px; letter-spacing: 1px;
    line-height: 40px;
    text-decoration: none;
  }
  .main-nav { position: absolute; top: 0; left: 0; height: 88px; width: 1200px; }
  .nav-link {
    position: absolute; top: 0; height: 88px;
    display: flex; align-items: center; justify-content: center;
    color: var(--white); text-decoration: none;
    font-size: 13px; font-weight: 500; text-transform: uppercase;
  }
  .nav-link.book { left: 615px; width: 73px; }
  .nav-link.how { left: 707px; width: 126px; }
  .nav-link.driver { left: 847px; width: 161px; background: var(--brand-blue-dark); }
  .nav-link.signin { left: 1022px; width: 81px; }

  .booking-panel {
    position: absolute; left: 86px; top: 151px;
    width: 1028px; height: 274px;
    background: var(--panel-bg);
    border: 1px solid var(--panel-border);
    border-radius: 3px;
  }
  .booking-title {
    position: absolute; left: 0; top: 80px; width: 100%;
    text-align: center;
    color: var(--heading-grey);
    font-size: 39px; font-weight: 500; line-height: 44px;
    text-transform: uppercase;
  }
  .booking-form {
    position: absolute; left: 295px; top: 152px;
  }
  .postal-input {
    position: absolute; left: 0; top: 0;
    width: 328px; height: 43px;
    border: 1px solid var(--input-border); border-radius: 3px;
    padding: 0 15px;
    font-family: "Roboto", Arial, sans-serif; font-size: 14px;
    color: var(--heading-grey); background: var(--white);
  }
  .postal-input::placeholder { color: var(--placeholder-grey); }
  .book-button {
    position: absolute; left: 334px; top: 0;
    width: 104px; height: 43px;
    border: none; border-radius: 3px;
    background: var(--brand-blue); color: var(--white);
    font-family: "Roboto", Arial, sans-serif;
    font-size: 17px; font-weight: 500;
  }

  .site-footer {
    position: absolute; left: 0; top: 489px;
    width: 1200px; height: 68px;
    background: var(--footer-bg);
  }
  .copyright {
    position: absolute; left: 86px; top: 26px;
    color: var(--white); font-size: 12.5px; font-weight: 700;
  }
  .social-links { position: absolute; left: 942px; top: 18px; display: flex; gap: 5px; }
  .social-link {
    width: 30px; height: 30px; border-radius: 50%;
    border: 1.5px solid var(--white); display: block;
  }
</style>
</head>
<body>
  <header class="site-header">
    <a class="brand" href="#">HAULVO</a>
    <nav class="main-nav">
      <a class="nav-link book" href="#">Book</a>
      <a class="nav-link how" href="#">How it works</a>
      <a class="nav-link driver" href="#">Become a driver</a>
      <a class="nav-link signin" href="#">Sign in</a>
    </nav>
  </header>

  <main class="booking-panel">
    <h1 class="booking-title">Need junk removed? Book now</h1>
    <form class="booking-form">
      <input class="postal-input" type="text" placeholder="Postal Code" aria-label="Postal Code">
      <button class="book-button" type="button">BOOK</button>
    </form>
  </main>

  <footer class="site-footer">
    <p class="copyright">© Copyright 2017 Haulvo.All Rights Reserved.</p>
    <div class="social-links">
      <a class="social-link" href="#" aria-label="Social link 1"></a>
      <a class="social-link" href="#" aria-label="Social link 2"></a>
      <a class="social-link" href="#" aria-label="Social link 3"></a>
      <a class="social-link" href="#" aria-label="Social link 4"></a>
      <a class="social-link" href="#" aria-label="Social link 5"></a>
    </div>
  </footer>
</body>
</html>
```